R&t Subterra

We specialize in CIPP pipe lining but do other underground utilities trenchless as well.

Target Market(s)

Trenchless sewer replacement

Contact Information for Business Card

Gavin Holtby 715-482-6130 Wisconsin rapids, wi

```html
<!DOCTYPE html>
<html lang="en">
<head>
<meta charset="utf-8">
<title>R&amp;T Subterra — Business Card</title>
<link rel="stylesheet" href="https://fonts.googleapis.com/css2?family=Montserrat:wght@400;500;700&display=swap">
<style>
  :root {
    --backdrop: #2b2b2d;
    --brand-blue: #5b8fcb;
    --brand-blue-light: #cfe3f7;
    --card-white: #ffffff;
    --ink-grey: #4a4a4a;
    --rule-grey: #8a8a8a;
  }
  * { box-sizing: border-box; margin: 0; padding: 0; }
  html, body {
    width: 1200px; height: 985px; overflow: hidden;
    background: var(--backdrop);
    font-family: "Montserrat", sans-serif;
  }
  .card {
    position: absolute; left: 290px;
    width: 620px; height: 354px;
    border-radius: 18px; overflow: hidden;
  }
  /* Back side */
  .card-back { top: 90px; background: var(--brand-blue); }
  .card-back .brand {
    position: absolute; inset: 0;
    display: flex; align-items: center; justify-content: center; gap: 18px;
  }
  .card-back .brand-dot {
    width: 62px; height: 62px; border-radius: 50%;
    background: var(--brand-blue-light);
  }
  .card-back .brand-name {
    font-weight: 700; font-size: 46px; color: var(--brand-blue-light);
    letter-spacing: 1px;
  }
  /* Front side */
  .card-front { top: 520px; background: var(--card-white); }
  .front-brand {
    position: absolute; top: 58px; right: 44px;
    display: flex; align-items: center; gap: 12px;
  }
  .front-brand .brand-dot {
    width: 40px; height: 40px; border-radius: 50%; background: var(--brand-blue);
  }
  .front-brand .brand-name {
    font-weight: 700; font-size: 30px; color: var(--brand-blue);
  }
  .person { position: absolute; top: 70px; left: 52px; }
  .person-name {
    font-weight: 700; font-size: 30px; color: var(--brand-blue); line-height: 1.1;
  }
  .person-title {
    font-weight: 400; font-size: 19px; color: var(--ink-grey); margin-top: 4px;
  }
  .rule-accent {
    position: absolute; top: 160px; left: 40px;
    width: 180px; height: 3px; background: var(--brand-blue);
  }
  .rule-thin {
    position: absolute; top: 161px; left: 220px;
    width: 360px; height: 1px; background: var(--rule-grey);
  }
  .contacts {
    position: absolute; top: 184px; left: 52px;
    list-style: none; font-size: 16px; color: var(--ink-grey);
  }
  .contacts li { display: flex; align-items: center; gap: 12px; height: 30px; }
  .contacts svg { width: 16px; height: 16px; fill: var(--brand-blue); flex: none; }
  .address {
    position: absolute; right: 44px; bottom: 42px;
    text-align: right; font-size: 17px; line-height: 1.45; color: var(--ink-grey);
  }
  .band {
    position: absolute; left: 0; right: 0; bottom: 0; height: 12px;
    background: linear-gradient(100deg, var(--brand-blue) 0 52%, var(--card-white) 52% 53%, var(--brand-blue) 53% 100%);
  }
</style>
</head>
<body>
  <section class="card card-back" aria-label="Card back">
    <div class="brand">
      <span class="brand-dot"></span>
      <span class="brand-name">R&amp;T Subterra</span>
    </div>
  </section>

  <section class="card card-front" aria-label="Card front">
    <div class="front-brand">
      <span class="brand-dot"></span>
      <span class="brand-name">R&amp;T Subterra</span>
    </div>

    <div class="person">
      <h1 class="person-name">Gavin Holtby</h1>
      <p class="person-title">Trial Attorney</p>
    </div>
    <div class="rule-accent"></div>
    <div class="rule-thin"></div>

    <ul class="contacts">
      <li>
        <svg viewBox="0 0 24 24" aria-hidden="true"><path d="M6.6 10.8a15 15 0 0 0 6.6 6.6l2.2-2.2a1 1 0 0 1 1-.25 11.4 11.4 0 0 0 3.6.57 1 1 0 0 1 1 1V20a1 1 0 0 1-1 1A17 17 0 0 1 3 4a1 1 0 0 1 1-1h3.5a1 1 0 0 1 1 1c0 1.25.2 2.45.57 3.6a1 1 0 0 1-.25 1z"/></svg>
        715-482-6130
      </li>
      <li>
        <svg viewBox="0 0 24 24" aria-hidden="true"><path d="M2 5h20v14H2zm2 2v.5l8 5 8-5V7l-8 5z"/></svg>
        GHoltby@rtsubterra.com
      </li>
      <li>
        <svg viewBox="0 0 24 24" aria-hidden="true"><path d="M12 2a10 10 0 1 0 0 20 10 10 0 0 0 0-20zm0 2c1.2 1.5 2 3.6 2.2 6H9.8C10 7.6 10.8 5.5 12 4zm-2.2 8h4.4c-.2 2.4-1 4.5-2.2 6-1.2-1.5-2-3.6-2.2-6zM4.1 12h3.7c.1 2 .6 3.9 1.4 5.4A8 8 0 0 1 4.1 12zm0-2a8 8 0 0 1 5.1-5.4C8.4 6.1 7.9 8 7.8 10zm12.1 0c-.1-2-.6-3.9-1.4-5.4A8 8 0 0 1 19.9 10zm0 2h3.7a8 8 0 0 1-5.1 5.4c.8-1.5 1.3-3.4 1.4-5.4z"/></svg>
        rtsubterra.com
      </li>
    </ul>

    <address class="address" style="font-style:normal">
      4120 Riverview Drive<br>
      Wisconsin Rapids, WI 54494
    </address>

    <div class="band"></div>
  </section>
</body>
</html>
```